vQ CARELINE (Brochure Design)

i need a proffesional brochure made. we are a mobile medical service company providing mobile Arterial Blood Gases(ABG's). Respiratory & Ventilator Consultation services. Ventilator and Tracheostomy training courses. and mobile vaccine administration.

this is my first time making a brochure so any and all advice/guidance will be appreciated.

i am thinking prints will be 8.5 inches x 11 inches (TRI-FOLD and BI-FOLD)

i have uploaded my business card design and logo design for reference.
as this brochure project continues ill update needs of the project descriptions.

Introduction: At vq CARELINE, we're dedicated to enhancing healthcare services by providing exceptional mobile arterial blood gases, respiratory and ventilator consultation services. Our core values revolve around excellence, compassion and accessibility. We believe that every individual deserves the highest standard of care, and we're committed to delivering that through expert guidance and top-notch training courses. Your health is at the heart of what we do, and we're here to support you on your journey to better respiratory health.

Mobile Arterial Blood Gases : Our mobile Arterial Blood Gas service offers quick, on-the-spot analysis of pH, oxygen, and carbon dioxide levels in your the blood. This service enables rapid adjustments to treatment plans for more effective respiratory care.

Ventilator and Tracheostomy Training: Our ventilator and tracheostomy course empowers caregivers and healthcare professionals to manage ventilators and care for tracheostomy patients with expertise. This training enhances patient safety, treatment outcomes, and healthcare provider confidence. vQ Careline your choice for top-notch care, convenience, and peace of mind.

Respiratory Consulting: Our respiratory consulting services provide expert guidance and support for individuals with respiratory / ventilator concerns. Benefits include personalized treatment plans, better management of respiratory conditions, and improved overall lung health. vQ Careline is your trusted partner for a breath of fresh air.

Target Market(s)

Sub-Acute facilities, Pulmonary Clinics, Pulmonologists, Nurses, Caregivers, Hospice and homehealth companies.

Industry/Entity Type

Medical; Respiratory; Nursing

Requirements
Must have
• proffesional simple design.

```html
<!DOCTYPE html>
<html lang="en">
<head>
<meta charset="utf-8">
<title>vQ CARELINE – Tri-fold Brochure</title>
<link rel="stylesheet" href="https://fonts.googleapis.com/css2?family=Roboto:wght@400;500;700&family=Roboto+Condensed:wght@700&family=Playfair+Display:wght@700&display=swap">
<style>
:root{
  --blue:#0f5db5;
  --blue-deep:#0a4fa0;
  --green:#1f9b3b;
  --green-light:#3fb14f;
  --line-green:#8ccf7e;
  --white:#ffffff;
  --paper:#ffffff;
  --grey-panel:#ededed;
  --ink:#2b2b2b;
  --backdrop:#d8d8d8;
}
*{box-sizing:border-box;margin:0;padding:0}
html,body{width:1200px;height:3491px;overflow:hidden}
body{background:var(--backdrop);font-family:"Roboto",Arial,sans-serif;color:var(--ink);position:relative}
.spread{position:absolute;left:60px;width:1080px;height:833px;display:flex;box-shadow:0 6px 18px rgba(0,0,0,.15)}
.spread--outside{top:882px}
.spread--inside{top:1775px}
.panel{position:relative;width:360px;height:100%;overflow:hidden}
.band{position:absolute;left:0;width:100%;height:16px}
.band--top{top:0}
.band--bottom{bottom:0}
.bg-blue{background:var(--blue)}
.bg-green{background:var(--green)}

/* outside */
.panel--consulting{background:var(--blue);color:var(--white)}
.panel--contact{background:var(--green);color:var(--white)}
.panel--cover{background:var(--white)}
.heading{font-family:"Roboto Condensed","Roboto",sans-serif;font-weight:700;font-size:17px;display:inline-block;padding:0 6px 3px 0;border-bottom:2px solid var(--line-green);border-right:2px solid var(--line-green)}
.panel--consulting .heading{position:absolute;left:55px;top:74px;color:var(--white)}
.copy{font-size:14px;line-height:18px}
.panel--consulting .copy{position:absolute;left:55px;top:114px;width:260px}
.service{position:absolute;left:0;width:100%;text-align:center;font-weight:500;font-size:16px;line-height:18px}
.service__icon{display:block;margin:0 auto 6px;width:78px;height:78px}
.service--1{top:366px}.service--2{top:514px}.service--3{top:658px}

.brand{display:flex;align-items:center;gap:8px;font-family:"Roboto",sans-serif;font-weight:500;letter-spacing:.5px}
.brand__mark{width:16px;height:16px;display:inline-block}
.panel--contact .brand{position:absolute;left:90px;top:532px;font-size:20px;color:var(--white);padding:4px 8px 4px 0;border-bottom:2px solid var(--line-green);border-right:2px solid var(--line-green)}
.panel--contact .brand__mark{background:var(--white)}
.contact{position:absolute;left:0;width:100%;display:flex;justify-content:center;align-items:center;gap:10px}
.contact svg{flex:none}
.contact--phone{top:604px;font-size:28px}
.contact--fax{top:643px;font-size:28px}
.contact--mail{top:698px;font-size:14px;font-weight:500;letter-spacing:.4px}
.contact--web{top:732px;font-size:14px;font-weight:500;letter-spacing:.4px}

.cover-head{position:absolute;left:0;top:16px;width:100%;height:168px;background:var(--white)}
.panel--cover .brand{position:absolute;left:42px;top:56px;font-size:28px;color:var(--blue);padding:6px 10px 6px 0;border-bottom:2px solid var(--line-green);border-right:2px solid var(--line-green)}
.panel--cover .brand__mark{width:30px;height:30px;background:var(--blue)}
.cover-slant{position:absolute;left:0;top:150px;width:360px;height:44px}
.cover-tag{position:absolute;left:0;top:184px;width:100%;height:206px;background:var(--blue);text-align:center;font-family:"Playfair Display",Georgia,serif;font-weight:700}
.cover-tag__lead{margin-top:28px;font-size:18px;color:var(--white)}
.cover-tag__title{margin-top:18px;font-size:37px;line-height:44px;color:var(--green-light)}
.photo{display:block}
.photo--cover{position:absolute;left:0;top:390px;width:360px;height:427px;background:linear-gradient(160deg,#cfe0f5 0%,#9cbde4 45%,#e9f0f9 100%)}

/* inside */
.panel--intro,.panel--training{background:var(--paper)}
.panel--abg{background:var(--grey-panel)}
.inside-head{position:absolute;left:0;top:16px;width:100%;height:48px;background:var(--white)}
.panel--intro .brand{position:absolute;left:24px;top:22px;font-size:14px;color:var(--blue);padding:2px 6px 2px 0;border-bottom:1px solid var(--line-green);border-right:1px solid var(--line-green)}
.panel--intro .brand__mark{width:14px;height:14px;background:var(--blue)}
.inside-slant{position:absolute;left:0;top:46px;width:1080px;height:30px;pointer-events:none}
.panel .heading--dark{position:absolute;top:92px;color:var(--blue)}
.panel--intro .heading--dark{left:43px}
.panel--abg .heading--dark,.panel--training .heading--dark{left:26px}
.panel--training .heading--dark{left:12px}
.photo--intro{position:absolute;left:31px;top:186px;width:288px;height:203px;background:linear-gradient(135deg,#6a4b8c 0%,#9a8bb0 40%,#c9ccd6 100%)}
.panel--intro .copy{position:absolute;left:31px;top:422px;width:296px;line-height:23.5px;font-size:13.6px}
.panel--abg .copy{position:absolute;left:26px;top:140px;width:312px;line-height:23.5px;font-size:13.6px}
.abg-card{position:absolute;left:26px;top:296px;width:312px;height:306px;background:var(--white)}
.abg-card__title{position:absolute;top:18px;width:100%;text-align:center;font-size:13.6px;font-weight:500}
.abg-table{position:absolute;left:18px;top:62px;width:162px;border-collapse:collapse;font-size:11px;text-align:center;border:1px solid #555}
.abg-table th,.abg-table td{border:1px solid #888;padding:3px 2px;line-height:13px}
.abg-table th{font-weight:500}
.photo--artery{position:absolute;left:188px;top:54px;width:112px;height:242px;background:linear-gradient(180deg,#f3e5df 0%,#d99c86 60%,#b86a55 100%);border-radius:40px 40px 10px 10px}
.photo--draw{position:absolute;left:26px;top:620px;width:312px;height:118px;background:linear-gradient(90deg,#e8eef6 0%,#7fa2d6 45%,#3c6fc1 70%,#e7e2df 100%)}
.panel--training .copy{position:absolute;left:26px;top:140px;width:310px;line-height:23.5px;font-size:13.6px}
.photo--vent{position:absolute;background:linear-gradient(160deg,#eef3fb 0%,#a9c3e6 50%,#dfe6f0 100%);border-radius:6px}
.photo--vent-a{left:54px;top:422px;width:244px;height:128px}
.photo--vent-b{left:54px;top:580px;width:110px;height:130px}
.photo--vent-c{left:198px;top:580px;width:100px;height:130px;background:linear-gradient(160deg,#f5f5fa 0%,#c9c8de 50%,#5c5a9a 100%)}
</style>
</head>
<body>

<!-- Outside of the brochure -->
<section class="spread spread--outside">
  <article class="panel panel--consulting">
    <div class="band band--top bg-green"></div>
    <h2 class="heading">Respiratory Consulting</h2>
    <p class="copy">Our respiratory consulting services provide expert guidance and support for individuals with respiratory / ventilator concerns. Benefits include personalized treatment plans, better management of respiratory conditions, and improved overall lung health. vQ Careline is your trusted partner for a breath of fresh air.</p>

    <div class="service service--1">
      <svg class="service__icon" viewBox="0 0 78 78"><circle cx="39" cy="39" r="36" fill="none" stroke="#fff" stroke-width="2.5"/><circle cx="39" cy="39" r="30" fill="#fff"/><path d="M37 22v14M41 22v14" stroke="#0f5db5" stroke-width="3" stroke-linecap="round"/><path d="M35 32c-6 0-13 8-13 18 0 5 4 6 8 4l5-3z" fill="#0f5db5"/><path d="M43 32c6 0 13 8 13 18 0 5-4 6-8 4l-5-3z" fill="#0f5db5"/></svg>
      Respiratory<br>Consultations
    </div>
    <div class="service service--2">
      <svg class="service__icon" viewBox="0 0 78 78"><circle cx="39" cy="39" r="36" fill="none" stroke="#fff" stroke-width="2.5"/><circle cx="39" cy="39" r="30" fill="#fff"/><g transform="rotate(45 39 42)"><rect x="34" y="28" width="10" height="24" fill="#0f5db5"/><rect x="31" y="26" width="16" height="3" fill="#0f5db5"/><rect x="37" y="52" width="4" height="4" fill="#0f5db5"/><line x1="39" y1="56" x2="39" y2="64" stroke="#0f5db5" stroke-width="1.5"/><rect x="37" y="20" width="4" height="6" fill="#0f5db5"/></g><path d="M52 18c2 3 3 5 3 6a3 3 0 0 1-6 0c0-1 1-3 3-6z" fill="#0f5db5"/></svg>
      In-house<br>ABG's
    </div>
    <div class="service service--3">
      <svg class="service__icon" viewBox="0 0 78 78"><circle cx="39" cy="39" r="36" fill="none" stroke="#fff" stroke-width="2.5"/><circle cx="39" cy="39" r="30" fill="#fff"/><rect x="24" y="22" width="22" height="16" rx="2" fill="none" stroke="#0f5db5" stroke-width="2.5"/><polyline points="27,31 31,31 33,26 36,35 38,31 43,31" fill="none" stroke="#0f5db5" stroke-width="1.6"/><rect x="26" y="40" width="18" height="14" rx="2" fill="#0f5db5"/><path d="M44 46c8 0 8 -8 12 -8" fill="none" stroke="#0f5db5" stroke-width="2"/><rect x="52" y="38" width="6" height="12" rx="3" fill="none" stroke="#0f5db5" stroke-width="2"/></svg>
      Ventilator<br>Training
    </div>
    <div class="band band--bottom bg-green"></div>
  </article>

  <article class="panel panel--contact">
    <div class="band band--top bg-blue"></div>
    <div class="brand"><span class="brand__mark"></span>vQ CARELINE</div>
    <div class="contact contact--phone">
      <svg width="24" height="24" viewBox="0 0 24 24"><path d="M6.6 10.8c1.4 2.8 3.8 5.1 6.6 6.6l2.2-2.2c.3-.3.7-.4 1-.2 1.1.4 2.3.6 3.6.6.6 0 1 .4 1 1V20c0 .6-.4 1-1 1C10.6 21 3 13.4 3 4c0-.6.4-1 1-1h3.5c.6 0 1 .4 1 1 0 1.3.2 2.5.6 3.6.1.3 0 .7-.2 1z" fill="#fff"/></svg>
      <span>555.010.2994</span>
    </div>
    <div class="contact contact--fax">
      <svg width="26" height="24" viewBox="0 0 26 24"><rect x="6" y="1" width="14" height="8" fill="none" stroke="#fff" stroke-width="2"/><rect x="1" y="9" width="24" height="14" fill="#fff"/><text x="13" y="20" font-family="Roboto,sans-serif" font-size="8" font-weight="700" fill="#1f9b3b" text-anchor="middle">FAX</text></svg>
      <span>555.010.2223</span>
    </div>
    <div class="contact contact--mail">
      <svg width="14" height="11" viewBox="0 0 14 11"><rect width="14" height="11" fill="#fff"/><polyline points="0,0 7,6 14,0" fill="none" stroke="#1f9b3b" stroke-width="1.4"/></svg>
      <span>info@vqcarelinegroup.com</span>
    </div>
    <div class="contact contact--web">
      <svg width="14" height="14" viewBox="0 0 14 14"><circle cx="7" cy="7" r="6" fill="none" stroke="#fff" stroke-width="1.4"/><ellipse cx="7" cy="7" rx="2.6" ry="6" fill="none" stroke="#fff" stroke-width="1.2"/><line x1="1" y1="7" x2="13" y2="7" stroke="#fff" stroke-width="1.2"/></svg>
      <span>vqcarelinegroup.com</span>
    </div>
    <div class="band band--bottom bg-blue"></div>
  </article>

  <article class="panel panel--cover">
    <div class="band band--top bg-green"></div>
    <div class="cover-head">
      <div class="brand"><span class="brand__mark"></span>vQ CARELINE</div>
    </div>
    <svg class="cover-slant" viewBox="0 0 360 44" preserveAspectRatio="none"><polygon points="0,34 280,34 300,10 360,10 360,44 0,44" fill="#0f5db5"/><polyline points="0,30 276,30 296,6 360,6" fill="none" stroke="#8ccf7e" stroke-width="2"/></svg>
    <div class="cover-tag">
      <p class="cover-tag__lead">Elevate Care, Empower Lives:</p>
      <h1 class="cover-tag__title">Your Health,<br>Our Priority</h1>
    </div>
    <div class="photo photo--cover" role="img" aria-label="Photo of a patient resting in a hospital bed beside a ventilator, with a nurse in blue scrubs"></div>
    <div class="band band--bottom bg-green"></div>
  </article>
</section>

<!-- Inside of the brochure -->
<section class="spread spread--inside">
  <article class="panel panel--intro">
    <div class="band band--top bg-blue"></div>
    <div class="inside-head"><div class="brand"><span class="brand__mark"></span>vQ CARELINE</div></div>
    <h2 class="heading heading--dark">Introduction</h2>
    <div class="photo photo--intro" role="img" aria-label="Photo of a nurse in purple scrubs adjusting a ventilator beside a patient in bed"></div>
    <p class="copy">At vQ CARELINE, we're dedicated to enhancing healthcare services by providing exceptional mobile arterial blood gases, respiratory and ventilator consultation services. Our core values revolve around excellence, compassion and accessibility. We believe that every individual deserves the highest standard of care, and we're committed to delivering that through expert guidance and top-notch training courses. Your health is at the heart of what we do, and we're here to support you on your journey to better respiratory health.</p>
    <div class="band band--bottom bg-blue"></div>
  </article>

  <article class="panel panel--abg">
    <div class="band band--top bg-green"></div>
    <div class="inside-head"></div>
    <h2 class="heading heading--dark">Mobile Arterial Blood Gases</h2>
    <p class="copy">Our mobile Arterial Blood Gas service offers quick, on-the-spot analysis of pH, oxygen, and carbon dioxide levels in your the blood. This service enables rapid adjustments to treatment plans for more effective respiratory care.</p>
    <div class="abg-card">
      <p class="abg-card__title">Arterial Blood Gas (ABG)</p>
      <table class="abg-table">
        <tr><th>ABG</th><th>Normal range</th></tr>
        <tr><td>O<sub>2</sub>CT</td><td>15-23% per<br>100 mL of blood</td></tr>
        <tr><td>pH</td><td>7.35-7.45</td></tr>
        <tr><td>PaCO<sub>2</sub></td><td>35-45 mmHg</td></tr>
        <tr><td>PaO<sub>2</sub></td><td>80-100 mmHg</td></tr>
        <tr><td>HCO<sub>3</sub></td><td>22-26 mEq/L</td></tr>
        <tr><td>O<sub>2</sub>Sat</td><td>95-100%</td></tr>
      </table>
      <div class="photo photo--artery" role="img" aria-label="Illustration of a forearm and hand showing the radial artery with a syringe drawing blood"></div>
    </div>
    <div class="photo photo--draw" role="img" aria-label="Photo of gloved hands taking an arterial blood sample from a wrist, with a close-up inset of the syringe"></div>
    <div class="band band--bottom bg-green"></div>
  </article>

  <article class="panel panel--training">
    <div class="band band--top bg-blue"></div>
    <div class="inside-head"></div>
    <h2 class="heading heading--dark">Ventilator and Tracheostomy Training</h2>
    <p class="copy">Our ventilator and tracheostomy course empowers caregivers and healthcare professionals to manage ventilators and care for tracheostomy patients with expertise. This training enhances patient safety, treatment outcomes, and healthcare provider confidence. vQ Careline your choice for top-notch care, convenience, and peace of mind.</p>
    <div class="photo photo--vent photo--vent-a" role="img" aria-label="Photo of two portable home ventilators with screens"></div>
    <div class="photo photo--vent photo--vent-b" role="img" aria-label="Photo of a compact portable ventilator with carry handle"></div>
    <div class="photo photo--vent photo--vent-c" role="img" aria-label="Photo of a portable ventilator with control panel"></div>
    <div class="band band--bottom bg-blue"></div>
  </article>

  <svg class="inside-slant" style="position:absolute;left:0;top:46px" viewBox="0 0 1080 30" preserveAspectRatio="none"><polyline points="0,26 1000,26 1030,2 1080,2" fill="none" stroke="#8ccf7e" stroke-width="2"/></svg>
</section>

</body>
</html>
```